Tri-fold 8.5x11" brochure for my company's service

I am looking for a brochure design (to be used with Bramwell Mart printing service-- their templates have been included) for my company, Quillstone Scholastics. We host, support, and provide custom programming for the open-source product, Quillstone (which we also created).

I have included a Notes file, which provides more potential copy and points about the company. Please read it thoroughly, but feel free to experiment, edit, only use pieces of text, etc. Don't feel like you have to follow anything in there exactly.

I have included a couple different versions of our logo.

I have also included a zip file of several nice-looking screenshots from our software.

I have also included a zip file of stock photos I have purchased, but feel free to use other ones if you like-- You can use free watermarked versions and I will purchase the full image later and add it in. You also don't have to use the stock photos at all; your choice.

I can make my way around Gimp and Photoshop, so the final product MUST be in a format (with different image and text layers) I can edit myself later for final tweaks. I can work with psd and xcf (gimp) files. If you prefer to work with Illustrator or InDesign, please check google; there are several answers for how to convert to a layered psd file.

Final product must be in 300 DPI, per the printer's instructions. If you have to use lower-res versions of images (like for unpaid stock photos) that's OK as long as you give me the URL to buy to full version; I can place the full size images myself.

Target Market(s)

University / College faculty, registrars, administrators, VP's, presidents, etc.

Industry/Entity Type

Higher Education, Universities, Colleges, Student Success

Font styles to use
Serif
Sans Serif
Other font styles liked:
• MONTSERRAT is the font used in my logo, I use RALEWAY on the website. But these are not requirements-- Use what you think looks best.

Colors

Designer to choose colors to be used in the design.

Requirements
Must have
• The final product MUST be in a format (with different image and text layers) that I can edit myself later for final tweaks. I can work with psd and xcf (gimp) files. 300dpi required by printer. Follow the template files included for exact measurements. If you prefer to work with Illustrator or InDesign, please check google; there are several answers for how to convert to a layered psd file.
Nice to have
• I would like (if possible) to mention that the software, Quillstone is open source. I feel like that is a big selling point for universities. Also, please try to have a similar look and feel as the website: quillstonescholastics.example, if possible. If possible, you can mention that our service runs on state-of-the-art cloud based hardware, though this is not a requirement. Also, try to work in "affordable pricing" and/or "great for schools of all sizes", or similar, if possible. One of our selling points is that we are much less expensive than our competitors.
Should not have
• Big walls of text. I appreciate trying to cram in a lot of information from my notes, but too much and it can look very crowded.

```html
<!DOCTYPE html>
<html lang="en">
<head>
<meta charset="utf-8">
<title>Quillstone Scholastics Tri-fold Brochure</title>
<link rel="stylesheet" href="https://fonts.googleapis.com/css2?family=Montserrat:wght@400;600;700;800&family=Raleway:wght@400;500;600&display=swap">
<style>
:root{
  --bg:#e9eaec;
  --paper:#ffffff;
  --ink:#2b2f3a;
  --muted:#5f6470;
  --pink:#e4287c;
  --blue:#1e9bd7;
  --orange:#f7941d;
  --purple:#7b4fa0;
  --navy:#243447;
  --photo-a:#8d9aa8;
  --photo-b:#c9b7a3;
  --screen-a:#dfe6ee;
  --screen-b:#aab8c6;
}
*{box-sizing:border-box;margin:0;padding:0}
html,body{width:900px;height:1200px;overflow:hidden}
body{background:var(--bg);font-family:'Raleway',sans-serif;color:var(--ink);padding:20px 80px}
.spread{width:740px;height:572px;background:var(--paper);display:grid;grid-template-columns:repeat(3,1fr);box-shadow:0 2px 10px rgba(0,0,0,.15)}
.spread + .spread{margin-top:16px}
.panel{position:relative;padding:18px 18px 0;border-right:1px solid #eceef1;display:flex;flex-direction:column;overflow:hidden}
.panel:last-child{border-right:none}
.brand{display:flex;align-items:center;gap:7px}
.brand-mark{width:14px;height:14px;background:var(--pink)}
.brand-name{font-family:'Montserrat',sans-serif;font-weight:700;font-size:13px;color:var(--navy);text-transform:uppercase;letter-spacing:.5px;line-height:1.1}
.photo{background:linear-gradient(135deg,var(--photo-a),var(--photo-b));border-radius:2px}
.screens{background:linear-gradient(160deg,var(--screen-a),var(--screen-b));border-radius:4px}
.body-text{font-size:9.5px;line-height:1.5;color:var(--muted)}
.section-title{font-family:'Montserrat',sans-serif;font-weight:800;font-size:15px;color:var(--pink);margin:12px 0 6px}
.feature-list{list-style:none;margin-top:8px}
.feature-list li{font-size:9.5px;color:var(--ink);padding:5px 0 5px 16px;border-bottom:1px dotted #d5d8dd;position:relative}
.feature-list li::before{content:"";position:absolute;left:0;top:8px;width:8px;height:8px;border-radius:50%;background:var(--blue)}
.feature-list li:nth-child(3n+2)::before{background:var(--pink)}
.feature-list li:nth-child(3n)::before{background:var(--orange)}
.headline{font-family:'Montserrat',sans-serif;font-weight:800;font-size:26px;line-height:1.05;color:var(--navy);text-transform:uppercase}
.headline .accent{color:var(--orange)}
.phone-line{display:flex;align-items:center;gap:8px;font-family:'Montserrat',sans-serif;font-weight:800;font-size:20px;color:var(--orange)}
.url{font-size:9px;color:var(--muted);margin-top:4px}
.color-bar{position:absolute;left:0;right:0;bottom:0;height:24px;display:flex}
.color-bar span{flex:1;display:flex;align-items:center;justify-content:center;font-family:'Montserrat',sans-serif;font-weight:700;font-size:9px;color:#fff;letter-spacing:.6px}
.c-pink{background:var(--pink)}.c-blue{background:var(--blue)}.c-orange{background:var(--orange)}.c-purple{background:var(--purple)}
.band{margin:12px -18px 10px;padding:7px 18px;font-family:'Montserrat',sans-serif;font-weight:800;font-size:12px;color:#fff;text-transform:uppercase;line-height:1.2}
.band.pink{background:var(--pink)}.band.blue{background:var(--blue)}
.lead{font-family:'Montserrat',sans-serif;font-weight:700;font-size:11.5px;line-height:1.3;color:var(--navy);text-transform:uppercase;margin-bottom:10px}
.fact{display:flex;gap:10px;align-items:flex-start;margin-bottom:12px}
.fact-icon{flex:none;width:30px;height:30px;border-radius:50%;display:flex;align-items:center;justify-content:center}
.fact h4{font-family:'Montserrat',sans-serif;font-weight:700;font-size:10.5px;color:var(--navy);text-transform:uppercase}
.fact p{font-size:9.5px;color:var(--muted);line-height:1.4}
.row{display:flex;gap:8px;align-items:center;padding:7px 0;border-bottom:1px solid #eceef1;font-size:9.5px;color:var(--ink)}
.row-icon{flex:none;width:18px;height:18px;border-radius:3px;display:flex;align-items:center;justify-content:center}
</style>
</head>
<body>

<section class="spread outside">
  <div class="panel inside-flap">
    <div class="photo" role="img" aria-label="Photo of students working together at laptops" style="height:140px;margin:-18px -18px 12px"></div>
    <p class="body-text">Quillstone helps faculty and advisors track student progress, flag early concerns and coordinate support across campus.</p>
    <h3 class="section-title">THE FEATURES</h3>
    <p class="body-text">Quillstone is an open-source, cloud-hosted platform built for schools of all sizes at affordable pricing.</p>
    <ul class="feature-list">
      <li>Early alerts and referrals</li>
      <li>Advising notes and appointments</li>
      <li>Attendance and progress reports</li>
      <li>Custom programming on request</li>
      <li>Secure state-of-the-art cloud hosting</li>
    </ul>
  </div>

  <div class="panel back-panel">
    <p class="body-text" style="margin-top:40px">Questions? Contact our team for a free demo of Quillstone.</p>
    <div class="brand" style="margin-top:40px"><span class="brand-mark"></span><span class="brand-name">Quillstone Scholastics</span></div>
    <h2 class="headline" style="margin-top:22px">Intuitive and <span class="accent">Powerful</span></h2>
    <p class="section-title" style="color:var(--blue);font-size:12px;margin-top:24px">CALL TODAY</p>
    <div class="phone-line">
      <svg width="18" height="18" viewBox="0 0 24 24" aria-hidden="true"><path fill="currentColor" d="M6.6 10.8a15 15 0 006.6 6.6l2.2-2.2a1 1 0 011-.25 11.4 11.4 0 003.6.57 1 1 0 011 1V20a1 1 0 01-1 1A17 17 0 013 4a1 1 0 011-1h3.5a1 1 0 011 1c0 1.25.2 2.45.57 3.57a1 1 0 01-.25 1z"/></svg>
      318-555-0147
    </div>
    <p class="url">quillstonescholastics.example</p>
    <div class="color-bar"><span class="c-pink"></span><span class="c-blue"></span><span class="c-orange"></span></div>
  </div>

  <div class="panel cover">
    <div class="brand"><span class="brand-mark"></span><span class="brand-name">Quillstone Scholastics</span></div>
    <div class="photo" role="img" aria-label="Photo of a college advisor meeting with a student" style="height:150px;margin:14px -18px 14px"></div>
    <h1 class="headline">Intuitive and <span class="accent">Powerful</span></h1>
    <p class="body-text" style="margin-top:4px;text-transform:uppercase;letter-spacing:1px">student success software</p>
    <div class="screens" role="img" aria-label="Software screenshots shown on laptop, tablet and phone" style="height:110px;margin-top:14px"></div>
    <div class="color-bar"><span class="c-blue">CLOUD HOSTED</span><span class="c-orange">OPEN SOURCE</span></div>
  </div>
</section>

<section class="spread inside">
  <div class="panel facts">
    <div class="brand"><span class="brand-mark"></span><span class="brand-name">Quillstone Scholastics</span></div>
    <div class="band pink">Facts at a glance</div>
    <p class="lead">Quillstone is a powerful Student Success Management System</p>
    <div class="fact"><span class="fact-icon c-pink"><svg width="14" height="14" viewBox="0 0 24 24" aria-hidden="true"><path d="M4 12l5 5L20 6" stroke="#fff" stroke-width="3" fill="none"/></svg></span><div><h4>Open Source</h4><p>No license fees, full transparency.</p></div></div>
    <div class="fact"><span class="fact-icon c-blue"><svg width="14" height="14" viewBox="0 0 24 24" aria-hidden="true"><path d="M4 12l5 5L20 6" stroke="#fff" stroke-width="3" fill="none"/></svg></span><div><h4>Cloud Hosted</h4><p>Fast, secure and always available.</p></div></div>
    <div class="fact"><span class="fact-icon c-orange"><svg width="14" height="14" viewBox="0 0 24 24" aria-hidden="true"><path d="M4 12l5 5L20 6" stroke="#fff" stroke-width="3" fill="none"/></svg></span><div><h4>Affordable</h4><p>Great for schools of all sizes.</p></div></div>
    <p class="body-text" style="margin-top:6px">Hosting, support and custom programming from the team that built Quillstone.</p>
    <div class="color-bar" style="height:10px"><span class="c-pink"></span></div>
  </div>

  <div class="panel welcome">
    <div class="band blue" style="margin-top:-6px">Welcome to<br>Quillstone Scholastics</div>
    <div class="photo" role="img" aria-label="Photo of students studying in a campus library" style="height:140px;margin-bottom:12px"></div>
    <p class="body-text">We created Quillstone and now host, support and extend it for colleges and universities nationwide.</p>
    <ul class="feature-list">
      <li>Dedicated support staff</li>
      <li>Custom reports and modules</li>
      <li>Smooth data migration</li>
      <li>Training for every campus</li>
    </ul>
    <div class="color-bar" style="height:10px"><span class="c-blue"></span></div>
  </div>

  <div class="panel platform">
    <div class="screens" role="img" aria-label="Software dashboard screenshots on a laptop and tablet" style="height:150px;margin-bottom:12px"></div>
    <div class="row"><span class="row-icon c-pink"></span>Access from any desktop, tablet or phone.</div>
    <div class="row"><span class="row-icon c-blue"></span>Role based views for advisors and staff.</div>
    <div class="row"><span class="row-icon c-orange"></span>Regular updates and new features.</div>
    <div class="row"><span class="row-icon c-purple"></span>Reliable backups every single day.</div>
    <div class="color-bar"><span class="c-pink"></span><span class="c-blue"></span><span class="c-orange"></span></div>
  </div>
</section>

</body>
</html>
```